VOLA New York *Luxury Candles*

We need a logo AND package design for a new private label luxury candle company.
I'm an interior decorator. When you enter a space you can perceive design as a 3 dimensional experience. However, the perfect scent in a space makes your experience unforgettable and 4 dimensional. Scents have the power to evoke pleasure and bring back memories.
I want my costumer to have a luxurious experience from the moment they see the package, open it, smell, enjoy and use it to decorate their spaces.
We are looking for a clean design that reads SERA. I'm attaching some pictures for Inspiration.
The candle is approximately 4 inches high 3.5 inches wide (10.3cm high, 9cm wide).

The company's name is

VOLA
New York

Target Market(s)

Women between 27 and 50 who like design, elegance, and beautiful spaces.
They like to indulge and create their safety sanctuary at home.

Industry/Entity Type

It Company

Font styles to use
Sans Serif
Script

Requirements
Must have
• A design for the candle and a design for the gift box + logo
Nice to have
• Simplicity
• Elegance
• Efortless beauty
Should not have
• Many different colors
• Shouldn't be overdone

```html
<!DOCTYPE html>
<html lang="en">
<head>
<meta charset="utf-8">
<title>VOLA New York — Candle Packaging</title>
<link rel="stylesheet" href="https://fonts.googleapis.com/css2?family=Josefin+Sans:wght@200&family=Cormorant+Garamond:wght@700&display=swap">
<style>
  :root {
    --backdrop: #eeeeee;
    --navy: #2e3650;
    --cream: #e4e5dc;
    --paper: #ffffff;
    --gold: #c9a24a;
    --gold-deep: #b58a35;
  }
  * { margin: 0; padding: 0; box-sizing: border-box; }
  html, body { width: 1200px; height: 799px; overflow: hidden; background: var(--backdrop); }
  .canvas { position: relative; width: 1200px; height: 799px; }

  .marble {
    background: linear-gradient(135deg, var(--navy) 0%, #6f7488 25%, var(--cream) 45%, #8a8ea0 62%, var(--navy) 80%, var(--cream) 100%);
  }

  .gift-box {
    position: absolute; left: 150px; top: 190px; width: 420px; height: 360px;
  }
  .gift-box__lid-line {
    position: absolute; left: 0; right: 0; top: 62px; height: 4px; background: var(--gold);
  }
  .box-label {
    position: absolute; left: 100px; top: 150px; width: 170px; height: 160px;
    background: var(--paper); border: 2px solid var(--gold);
  }

  .candle-label {
    position: absolute; left: 700px; top: 285px; width: 275px; height: 265px; padding: 14px;
  }
  .candle-label__panel { width: 100%; height: 100%; background: var(--paper); }

  .mark {
    display: flex; flex-direction: column; align-items: center; justify-content: center;
    width: 100%; height: 100%; text-align: center;
  }
  .mark__name {
    font-family: "Josefin Sans", sans-serif; font-weight: 200; color: var(--gold);
    letter-spacing: 0.12em;
  }
  .mark__dot { border-radius: 50%; background: var(--navy); }
  .mark__place {
    font-family: "Cormorant Garamond", serif; font-weight: 700; color: var(--gold-deep);
    letter-spacing: 0.14em; line-height: 1.2;
  }

  .box-label .mark__name { font-size: 40px; margin-bottom: 14px; }
  .box-label .mark__dot { width: 4px; height: 4px; margin-bottom: 16px; }
  .box-label .mark__place { font-size: 9px; color: var(--navy); }

  .candle-label .mark__name { font-size: 62px; margin-bottom: 26px; }
  .candle-label .mark__dot { width: 6px; height: 6px; margin-bottom: 26px; }
  .candle-label .mark__place { font-size: 13px; }
</style>
</head>
<body>
<main class="canvas">
  <section class="gift-box marble" role="img" aria-label="Navy and cream marbled paper pattern covering the gift box">
    <div class="gift-box__lid-line"></div>
    <div class="box-label">
      <div class="mark">
        <span class="mark__name">SERA</span>
        <span class="mark__dot"></span>
        <span class="mark__place">VOLA<br>NEW YORK</span>
      </div>
    </div>
  </section>

  <section class="candle-label marble" role="img" aria-label="Navy and cream marbled border around the candle label">
    <div class="candle-label__panel">
      <div class="mark">
        <span class="mark__name">SERA</span>
        <span class="mark__dot"></span>
        <span class="mark__place">VOLA<br>NEW YORK</span>
      </div>
    </div>
  </section>
</main>
</body>
</html>
```